Game, Voice & Dedicated Server Company Needs a Business Card Design

We need a new business card design, centered around our new logo (PSD provided below).

Designs that we do like:
https://pixelmarsh.net/item/corporate-business-card/5382017?s_rank=43 (needs to be made more eye catching)

Our main areas of business are:
- Dedicated Servers
- Game Servers
- Voice Servers
- Mitigation Security Specialists

Industry/Entity Type

Business

Contact Information for Business Card

On the card: (and anything else you would suggest)
- Staff member name
- Staff member position in company
- Staff member phone number
- Staff member email
- Other / Staff member Skype
- Website link

Colors
9bcb3c
abd036

Requirements
Must have
• Design of Card:
• - Green (same green as the logo)
• - Business / Corporate design
• - Something a little different / abstract that shouts premium

```html
<!DOCTYPE html>
<html lang="en">
<head>
<meta charset="utf-8">
<title>Tidepath Hosting – Business Card</title>
<link rel="stylesheet" href="https://fonts.googleapis.com/css2?family=Archivo:wght@800&family=Montserrat:wght@300;400;700&family=Oswald:wght@500&display=swap">
<style>
  :root {
    --page-bg: #d9d9d7;
    --card-black: #201f20;
    --card-grey: #414342;
    --panel-dark: #2a2b33;
    --panel-grey: #47494b;
    --brand-green: #6db33f;
    --accent-green: #9bcb3c;
    --text-white: #ffffff;
    --text-soft: #e6e6e6;
  }
  * { margin: 0; padding: 0; box-sizing: border-box; }
  html, body { width: 1200px; height: 900px; overflow: hidden; }
  body {
    background: var(--page-bg);
    position: relative;
    font-family: "Montserrat", sans-serif;
  }
  .card {
    position: absolute;
    left: 250px;
    width: 700px;
    height: 400px;
    overflow: hidden;
    box-shadow: 0 10px 30px rgba(0,0,0,0.25);
  }
  .card--front { top: 30px; background: var(--card-black); }
  .card--details { top: 470px; background: var(--card-grey); }

  .brand {
    position: absolute;
    display: flex;
    align-items: center;
    gap: 22px;
  }
  .brand__square { width: 74px; height: 74px; background: var(--brand-green); }
  .brand__name {
    font-family: "Archivo", sans-serif;
    font-weight: 800;
    color: var(--brand-green);
    line-height: 0.95;
    letter-spacing: -0.5px;
  }
  .card--front .brand { left: 150px; top: 140px; }
  .card--front .brand__name { font-size: 46px; }

  .card--details .brand {
    left: 455px; top: 120px;
    flex-direction: column; align-items: flex-start; gap: 16px;
  }
  .card--details .brand__square { width: 64px; height: 64px; margin-left: 40px; }
  .card--details .brand__name { font-size: 34px; }

  .panels { position: absolute; inset: 0; }

  .person {
    position: absolute;
    right: 330px; top: 44px;
    text-align: right;
    color: var(--text-white);
  }
  .person__name { font-size: 27px; font-weight: 300; letter-spacing: 1px; }
  .person__name strong { font-weight: 700; }
  .person__role { font-size: 12px; font-weight: 400; letter-spacing: 5px; color: var(--text-soft); margin-top: 4px; }

  .contact {
    position: absolute;
    font-family: "Oswald", sans-serif;
    font-weight: 500;
    font-style: italic;
    color: var(--text-white);
    font-size: 21px;
    text-align: right;
  }
  .contact--phone { right: 368px; top: 126px; }
  .contact--email { right: 384px; top: 196px; font-size: 18px; }
  .contact--chat  { right: 400px; top: 266px; }

  .website {
    position: absolute;
    left: 468px; top: 330px;
    display: flex; align-items: center; gap: 8px;
    font-family: "Oswald", sans-serif;
    font-weight: 500;
    color: var(--accent-green);
    font-size: 18px;
  }
</style>
</head>
<body>

  <section class="card card--front">
    <div class="brand">
      <div class="brand__square"></div>
      <div class="brand__name">TIDEPATH<br>HOSTING</div>
    </div>
  </section>

  <section class="card card--details">
    <svg class="panels" width="700" height="400" viewBox="0 0 700 400">
      <polygon points="0,0 460,0 370,400 0,400" fill="var(--panel-dark)"/>
      <polygon points="0,8 452,8 447,28 0,28" fill="var(--brand-green)"/>
      <polygon points="0,36 440,36 425,104 0,104" fill="var(--panel-grey)"/>

      <polygon points="0,114 360,114 347,172 0,172" fill="var(--card-grey)"/>
      <polygon points="368,114 424,114 411,172 355,172" fill="var(--brand-green)"/>
      <polygon points="0,184 345,184 332,242 0,242" fill="var(--card-grey)"/>
      <polygon points="353,184 409,184 396,242 340,242" fill="var(--brand-green)"/>
      <polygon points="0,254 329,254 316,312 0,312" fill="var(--card-grey)"/>
      <polygon points="337,254 393,254 380,312 324,312" fill="var(--brand-green)"/>

      <polygon points="0,356 370,356 363,386 0,386" fill="var(--brand-green)"/>

      <!-- phone icon -->
      <g transform="translate(389,143)">
        <circle r="14" fill="var(--text-white)"/>
        <path d="M-6,-7 l4,-1 l2,5 l-3,2 q2,4 6,6 l2,-3 l5,2 l-1,4 q-9,1 -15,-15 z" fill="var(--brand-green)"/>
      </g>
      <!-- mail icon -->
      <g transform="translate(374,213)">
        <circle r="14" fill="var(--text-white)"/>
        <rect x="-7" y="-5" width="14" height="10" fill="var(--brand-green)"/>
        <path d="M-7,-5 L0,1 L7,-5" fill="none" stroke="var(--text-white)" stroke-width="1.5"/>
      </g>
      <!-- chat icon -->
      <g transform="translate(358,283)">
        <circle r="14" fill="var(--text-white)"/>
        <path d="M-7,-6 h14 v9 h-8 l-4,4 v-4 h-2 z" fill="var(--brand-green)"/>
      </g>
    </svg>

    <div class="person">
      <div class="person__name">ALEX <strong>MARLOW</strong></div>
      <div class="person__role">MANAGER</div>
    </div>
    <div class="contact contact--phone">202-555-0187</div>
    <div class="contact contact--email">alex.marlow@tidepathmail.com</div>
    <div class="contact contact--chat">alex.marlow</div>

    <div class="brand">
      <div class="brand__square"></div>
      <div class="brand__name">TIDEPATH<br>HOSTING</div>
    </div>

    <div class="website">
      <svg width="20" height="20" viewBox="0 0 20 20" aria-hidden="true">
        <circle cx="10" cy="10" r="8.5" fill="none" stroke="var(--text-white)" stroke-width="1.8"/>
        <ellipse cx="10" cy="10" rx="3.5" ry="8.5" fill="none" stroke="var(--text-white)" stroke-width="1.4"/>
        <line x1="1.5" y1="10" x2="18.5" y2="10" stroke="var(--text-white)" stroke-width="1.4"/>
      </svg>
      <span>www.tidepath-hosting.com</span>
    </div>
  </section>

</body>
</html>
```